A small boutique Accounting and Mortgage Broking firm needs a business card design

Quorvel is a Brisbane based boutique accounting and mortgage broking firm. We offer a range of extensive financial services like accounting, tax consulting, book-keeping and mortgage broking.
We need a business card that stands out. The content can stay as it is on the existing card unless you recommend us to change anything on it for a better design.
Please remove the mobile number and give us a suitable format to change the details like email address and name.
Industry/Entity Type
Business
Contact Information for Business Card
Dalian Okoruwe
Quorvel Group Pty Ltd
3/412 Brackwin Rd Tarrowby QLD 4192
PO Box 829 Tarrowby QLD 4192
T 07 3184 5526
F 07 3952 1087
E dokoruwe@quorvel.net.au
Accountants Tax Agents, Mortgage Brokers
www.quorvel.net.au
Look and feel
Each slider illustrates characteristics of the customer's brand and the style your logo design should communicate.

```html
<!DOCTYPE html>
<html lang="en">
<head>
<meta charset="utf-8">
<title>Quorvel Business Card</title>
<link rel="stylesheet" href="https://fonts.googleapis.com/css2?family=Open+Sans:wght@400;600;700&display=swap">
<style>
  :root {
    --green: #7cc243;
    --green-deep: #4cb648;
    --charcoal: #3a3a3a;
    --paper: #ffffff;
    --paper-shade: #e4e4e4;
    --backdrop: #eeeeea;
    --white: #ffffff;
  }
  * { box-sizing: border-box; margin: 0; padding: 0; }
  html, body {
    width: 1200px; height: 900px; overflow: hidden;
    background: var(--backdrop);
    font-family: "Open Sans", Arial, sans-serif;
  }
  .canvas {
    width: 1200px; height: 900px;
    display: flex; flex-direction: column;
    align-items: center; justify-content: center; gap: 56px;
  }
  .card {
    width: 640px; height: 366px;
    position: relative; overflow: hidden;
    box-shadow: 0 6px 18px rgba(0,0,0,0.18);
  }

  /* Front */
  .card-front {
    background: radial-gradient(ellipse at 30% 20%, var(--green-deep) 0%, var(--green) 70%);
    color: var(--white);
    display: flex; flex-direction: column; align-items: center; justify-content: center;
  }
  .brand { display: flex; align-items: center; gap: 12px; }
  .brand-dot {
    width: 52px; height: 52px; border-radius: 50%;
    border: 6px solid currentColor;
  }
  .brand-name { font-weight: 700; font-size: 54px; line-height: 1; letter-spacing: -1px; }
  .front-services { margin-top: 34px; font-size: 17px; letter-spacing: 0.3px; }
  .front-web { margin-top: 22px; font-size: 16px; }

  /* Back */
  .card-back { background: var(--green); }
  .back-top {
    height: 52%;
    background: linear-gradient(180deg, var(--paper) 0%, var(--paper) 55%, var(--paper-shade) 100%);
    display: flex; flex-direction: column; align-items: center; justify-content: center;
  }
  .card-back .brand { color: var(--charcoal); }
  .card-back .brand-dot { width: 60px; height: 60px; border-width: 8px; }
  .card-back .brand-name { font-size: 60px; }
  .tagline {
    margin-top: 8px; font-size: 26px; letter-spacing: -0.3px;
    color: var(--charcoal); font-weight: 400;
  }
  .back-details {
    height: 48%;
    display: flex; justify-content: space-between; gap: 26px;
    padding: 24px 32px 0 40px; color: var(--white);
  }
  .person { padding-top: 14px; text-align: right; }
  .person-name { font-weight: 700; font-size: 24px; margin-bottom: 10px; }
  .address { font-size: 17px; line-height: 1.35; }
  .contacts { list-style: none; padding-top: 4px; }
  .contacts li {
    display: flex; align-items: center; gap: 12px;
    font-size: 15px; margin-bottom: 8px;
  }
  .contact-icon {
    width: 20px; height: 20px; border-radius: 3px;
    background: var(--white); flex: none;
  }
</style>
</head>
<body>
<main class="canvas">
  <section class="card card-front">
    <div class="brand">
      <span class="brand-dot"></span>
      <span class="brand-name">quorvel</span>
    </div>
    <p class="front-services">Accountants - Tax Agents - Mortgage Brokers</p>
    <p class="front-web">www.quorvel.net.au</p>
  </section>

  <section class="card card-back">
    <div class="back-top">
      <div class="brand">
        <span class="brand-dot"></span>
        <span class="brand-name">quorvel</span>
      </div>
      <p class="tagline">CLARITY. CARE. PROGRESS.</p>
    </div>
    <div class="back-details">
      <div class="person">
        <p class="person-name">Dalian Okoruwe</p>
        <p class="address">3/412 Brackwin Rd Tarrowby QLD 4192<br>PO Box 829 Tarrowby QLD 4192</p>
      </div>
      <ul class="contacts">
        <li>
          <svg class="contact-icon" viewBox="0 0 20 20" aria-hidden="true">
            <path d="M6 4c1 0 2 3 2 3.5S7 9 7 9s1.5 3 4 4c0 0 1-1 1.5-1s3.5 1 3.5 2-1.5 2.5-2.5 2.5C9 16.5 3.5 11 3.5 6.5 3.5 5.5 5 4 6 4z" fill="#7cc243"/>
          </svg>
          <span>07 3184 5526</span>
        </li>
        <li>
          <svg class="contact-icon" viewBox="0 0 20 20" aria-hidden="true">
            <rect x="6" y="3.5" width="8" height="4" fill="none" stroke="#7cc243" stroke-width="1.5"/>
            <rect x="3.5" y="7.5" width="13" height="6" rx="1" fill="#7cc243"/>
            <rect x="6" y="12" width="8" height="4.5" fill="#fff" stroke="#7cc243" stroke-width="1.5"/>
          </svg>
          <span>07 3952 1087</span>
        </li>
        <li>
          <svg class="contact-icon" viewBox="0 0 20 20" aria-hidden="true">
            <rect x="3.5" y="5.5" width="13" height="9" fill="none" stroke="#7cc243" stroke-width="1.5"/>
            <path d="M3.5 5.5 10 11l6.5-5.5" fill="none" stroke="#7cc243" stroke-width="1.5"/>
          </svg>
          <span>dokoruwe@quorvel.net.au</span>
        </li>
      </ul>
    </div>
  </section>
</main>
</body>
</html>
```